Cultured Basics Website Design

We need a modern, elegant website for a nutritional product called "Cultured Basics" which is based on the diets of people living in Longevity Hot Spots. In Longevity Hot Spots people live uncommonly longer and healthier lives. Most of these Hot Spots are in exotic locations around the world. I have attached several images taken from the Hot Spot in Costa Rica, along with our Logo and the text for the entire website. It is not necessary to use/include all of the text, we can add and adjust that later. For now, we need the design for the home page and template for interior pages. You do not have to use the images we provide, we can purchase additional images if needed. "Final selection should include Adobe Muse template file and all supporting graphics in editable formats (PhotoShop, Illustrator, etc)" We have posted several projects on Sketch Harbor and have accepted in every case. We look forward to seeing your design for our website. Thanks!
We like the look of these websites as an example. You have to press "Preview" (which is located on the right) to see the website.
https://www.pagebloomer.com/websites/templates/drift
https://www.pagebloomer.com/websites/templates/marlow
35-60 80% female, 20% male
Product
1 page

```html
<!DOCTYPE html>
<html lang="en">
<head>
<meta charset="utf-8">
<title>Cultured Basics</title>
<link rel="stylesheet" href="https://fonts.googleapis.com/css2?family=Jost:wght@300;400;500;600&display=swap">
<style>
:root{
  --paper:#f1eff0;
  --ink:#2a2a2a;
  --green:#5a9a2a;
  --green-dark:#3f7d1c;
  --white:#ffffff;
  --footer:#3c3c3c;
  --footer-text:#b9b9b9;
  --band:rgba(3,28,26,.82);
  --panel:rgba(232,232,232,.93);
}
*{margin:0;padding:0;box-sizing:border-box}
html,body{width:1200px;height:2539px;overflow:hidden}
body{background:var(--paper);font-family:"Jost",sans-serif;color:var(--ink);font-weight:300;position:relative}
.site-header{position:absolute;top:0;left:0;width:1200px;height:93px;background:var(--paper)}
.brand{position:absolute;left:85px;top:26px;display:flex;align-items:center;gap:10px;font-size:30px;font-weight:400;color:var(--green);line-height:1}
.brand-dot{width:34px;height:34px;border-radius:50%;background:var(--green)}
.main-nav{position:absolute;right:88px;top:36px;display:flex;gap:48px}
.main-nav a{font-size:15px;color:var(--ink);text-decoration:none;font-weight:400}
.hero{position:absolute;top:93px;left:0;width:1200px;height:550px;
  background:linear-gradient(180deg,#a9c9df 0%,#d7e6ee 30%,#3f7a2c 45%,#2f6424 62%,#9c8a5b 76%,#c9d6dc 86%,#7ea3b8 100%)}
.welcome{position:absolute;top:643px;left:0;width:1200px;height:305px;text-align:center}
.welcome h1{position:absolute;top:88px;width:100%;font-size:27px;font-weight:300;color:var(--green)}
.welcome .claims{position:absolute;top:150px;width:100%;font-size:15px;font-weight:300}
.welcome .lede{position:absolute;top:178px;width:100%;font-size:13.5px;font-weight:300}
.story{position:absolute;top:948px;left:0;width:1200px;height:550px;
  background:linear-gradient(135deg,#1d4a42 0%,#5b4a3a 35%,#7a5a48 55%,#2f6b5c 80%,#1d4a42 100%)}
.story-band{position:absolute;top:102px;left:0;width:1200px;height:348px;background:var(--band);text-align:center;color:var(--white)}
.story-band h2{margin-top:50px;font-size:52px;font-weight:300;letter-spacing:1px;line-height:1}
.story-band p{width:900px;margin:26px auto 0;font-size:13.5px;line-height:24px;font-weight:300;color:var(--white)}
.btn{display:inline-block;width:226px;height:43px;line-height:37px;font-size:13px;font-weight:600;letter-spacing:2.5px;text-decoration:none;text-align:center}
.btn-light{border:3px solid var(--white);color:var(--white);margin-top:26px}
.btn-dark{border:3px solid #111;color:#111}
.benefits{position:absolute;top:1498px;left:0;width:1200px;height:271px;text-align:center;font-size:14px}
.benefits p{margin-top:67px}
.benefits ul{list-style:none;margin-top:5px}
.benefits li{color:var(--green-dark);line-height:25.8px}
.benefits li::before{content:"›";font-weight:600;margin-right:3px}
.product{position:absolute;top:1769px;left:0;width:1200px;height:547px;
  background:linear-gradient(110deg,#3b3029 0%,#4a3c32 40%,#c9776f 55%,#e0a04a 65%,#6a4a6a 75%,#b53a3a 88%,#3b3029 100%)}
.product-panel{position:absolute;left:86px;top:39px;width:456px;height:469px;background:var(--panel);padding:0 26px}
.product-panel h2{margin-top:50px;font-size:50px;font-weight:300;line-height:1;padding-left:30px}
.product-panel hr{border:0;border-top:1.5px solid #333;margin-top:22px}
.product-panel p{margin-top:18px;font-size:13.5px;line-height:24px;text-align:justify;font-weight:300}
.product-panel .btn{position:absolute;left:115px;top:372px}
.social{position:absolute;top:2316px;left:0;width:1200px;height:76px;display:flex;justify-content:center;align-items:center;gap:14px}
.social span{width:14px;height:14px;border-radius:50%;background:#333;display:block}
.site-footer{position:absolute;top:2392px;left:0;width:1200px;height:147px;background:var(--footer);text-align:center;color:var(--footer-text);font-size:12.5px}
.site-footer .address{margin-top:53px}
.site-footer .copyright{margin-top:9px}
.site-footer .copyright em{font-style:normal;color:var(--green)}
</style>
</head>
<body>
<header class="site-header">
  <div class="brand"><span class="brand-dot"></span>Cultured Basics</div>
  <nav class="main-nav"><a href="#">Our Story</a><a href="#">Our Product</a><a href="#">Shop Now</a><a href="#">Contact</a></nav>
</header>

<section class="hero" role="img" aria-label="Tropical beach with palm-covered green hillside under a blue sky"></section>

<section class="welcome">
  <h1>Welcome to Cultured Basics</h1>
  <p class="claims">Synthetic Free • Gluten Free • Soy Free • GMO Free • Vegan • NonDairy • No Fillers • No Trans Fat</p>
  <p class="lede">The world’s first and only retail foundational supplement based on research of the world’s healthiest people.</p>
</section>

<section class="story" role="img" aria-label="Group of village residents standing together on a porch">
  <div class="story-band">
    <h2>OUR STORY</h2>
    <p>While on a business trip to Costa Rica in 2004, lifelong entrepreneur Walter Reyes discovered a small village on the Nicoyan Peninsula where there are no hospitals and obesity, cancer and cardiovascular disease are virtually non existent. In this village of Nosara, people live healthy, vital lives well into their 90s and even past 100. Reyes was captivated by this discovery and he spent the next six years investigating this phenomenon. He learned it occurs only in eight other locales known as Vital Age Zones.</p>
    <a class="btn btn-light" href="#">READ MORE</a>
  </div>
</section>

<section class="benefits">
  <p>Mixed with your favorite juice, beverage or smoothie, each daily serving of Cultured Basics provides:</p>
  <ul>
    <li>11 of the most powerful fermented fruits, vegetables and herbs</li>
    <li>The probiotic equivalent of two servings of yogurt for digestive support</li>
    <li>The oat beta glucan equivalent of five servings of oatmeal for a healthy heart</li>
    <li>The resveratrol antioxidant power of 18 glasses of red wine</li>
  </ul>
</section>

<section class="product" role="img" aria-label="Smoothies, fruit bowls, berries, pomegranate and limes on a dark wooden table">
  <div class="product-panel">
    <h2>OUR PRODUCT</h2>
    <hr>
    <p>Over the past few decades our ability to eat healthily has become increasingly difficult as our food supply’s nutritional potency has been reduced by large-scale agricultural practices—including a reliance on antibiotics and the rampant use of processing with chemical cleansers. As a consequence, our overall health has been compromised, which is apparent in the rise of chronic disease in our culture. It has been reported that as much as 85% of health related issues in this country can be related back to nutritional aspects.</p>
    <a class="btn btn-dark" href="#">READ MORE</a>
  </div>
</section>

<div class="social">
  <span role="img" aria-label="Social link"></span>
  <span role="img" aria-label="Social link"></span>
  <span role="img" aria-label="Social link"></span>
</div>

<footer class="site-footer">
  <p class="address">The Palm Row Collective, 128 Harbor Lane, Costa Rica 000-555-0142</p>
  <p class="copyright">Copyright © 2016 <em>Cultured Basics</em>. All Rights Reserved.</p>
</footer>
</body>
</html>
```